Trifold Brochure Design Project

We need a trifold brochure design for a company/product called VitaLens. We provide full-body MRI screening, along with blood chemistry and DNA analysis, followed by a consultation with the MD in a comfortable outpatient setting.
The facility is located in Fort Lauderdale, Florida.
The concept is that people usually don't know about many diseases until they are far advanced and more difficult to treat. We offer early detection which leads to early treatment and better outcomes.
The concept should blend an emotional construct (do it for yourself or someone you love, the best gift is health, live longer to love longer, etc) with science to legitimize the service. (MRI, Blood Chemistry, DNA analysis and an MD to interpret)

Target Market(s)

Baby boomers and active middle-age men and women

Industry/Entity Type

It Company

Requirements
Must have
• Attractive middle age people enjoying life because they know they are healthy.
Services are provided 7-days a week in a comfortable outpatient setting. Everything is totally confidential.
VitaLens is a division of Coral Ridge Diagnostic Centers
Nice to have
• Some clinical imagery such as the doctor, the MRI machine or inferences that this is a clinical-based solution.
Extremely experienced, qualified and licensed Doctors and Technologists are involved.

```html
<!DOCTYPE html>
<html lang="en">
<head>
<meta charset="utf-8">
<title>VitaLens Trifold – Inside</title>
<link href="https://fonts.googleapis.com/css2?family=Oswald:wght@400;500&family=Arimo:wght@400&display=swap" rel="stylesheet">
<style>
  :root {
    --page-bg: #e8e5e1;
    --cream-top: #e3e2c6;
    --cream-bottom: #eeedd9;
    --paper: #ffffff;
    --ink-blue: #1d4f8b;
    --navy: #0d4580;
    --navy-deep: #083466;
    --navy-light: #15599a;
    --dna-violet: #4b3fc4;
    --dna-deep: #22309a;
    --portrait-tone: #e2d3cb;
    --portrait-warm: #ecc0ae;
    --scanner-light: #efe9e9;
    --scanner-mid: #d3c6c6;
    --mauve: #b09697;
    --mauve-dark: #8e7477;
    --white: #ffffff;
  }
  * { box-sizing: border-box; margin: 0; padding: 0; }
  html, body { width: 1200px; height: 1062px; overflow: hidden; }
  body { background: var(--page-bg); position: relative; font-family: "Arimo", Arial, sans-serif; }

  .brochure {
    position: absolute; left: 53px; top: 134px;
    width: 1100px; height: 830px;
    display: flex;
    box-shadow: 0 6px 24px rgba(0,0,0,0.25);
  }
  .panel { position: relative; height: 100%; overflow: hidden; }

  /* Inside left */
  .panel-left { width: 360px; background: var(--paper); }
  .director-photo {
    position: absolute; left: 0; top: 0; width: 360px; height: 386px;
    background: linear-gradient(180deg, var(--cream-top) 0%, var(--cream-bottom) 100%);
  }
  .portrait-frame {
    position: absolute; left: 51px; top: 40px;
    width: 249px; height: 249px;
    background: var(--white);
    transform: rotate(-18.9deg);
    box-shadow: 4px 8px 16px rgba(0,0,0,0.28);
    padding: 19px;
  }
  .portrait-photo {
    width: 100%; height: 100%;
    background: linear-gradient(180deg, var(--portrait-warm) 0%, var(--portrait-tone) 100%);
  }
  .left-copy {
    position: absolute; left: 42px; width: 292px;
    color: var(--ink-blue); font-size: 15px; line-height: 21px;
  }
  .left-copy.first { top: 394px; }
  .left-copy.second { top: 584px; }

  /* Inside center */
  .panel-center {
    width: 371px;
    background: radial-gradient(ellipse at 40% 25%, var(--navy-light) 0%, var(--navy) 55%, var(--navy-deep) 100%);
  }
  .science-art { position: absolute; left: 0; top: 0; width: 371px; height: 830px; }
  .services-title {
    position: absolute; left: 40px; top: 80px;
    font-family: "Oswald", "Arial Narrow", sans-serif; font-weight: 500;
    font-size: 33px; line-height: 40px; color: var(--white);
  }
  .services-box {
    position: absolute; left: 42px; top: 133px; width: 308px; height: 375px;
    border: 1px solid var(--white);
    padding: 9px 9px;
    color: var(--white); font-size: 15px; line-height: 21px;
  }
  .services-box p + p { margin-top: 6px; }

  /* Inside right */
  .panel-right {
    width: 369px;
    background: linear-gradient(180deg, var(--mauve) 0%, var(--mauve-dark) 100%);
  }
  .scanner-photo {
    position: absolute; left: 0; top: 0; width: 369px; height: 397px;
    background: linear-gradient(160deg, var(--scanner-mid) 0%, var(--scanner-light) 45%, var(--scanner-mid) 100%);
  }
  .right-headline {
    position: absolute; left: 55px; top: 410px; width: 300px;
    font-family: "Oswald", "Arial Narrow", sans-serif; font-weight: 500;
    font-size: 30px; line-height: 33px; color: var(--white);
  }
  .right-body {
    position: absolute; left: 55px; top: 604px; width: 300px;
    font-size: 21px; line-height: 34px; color: var(--white);
  }
</style>
</head>
<body>
  <main class="brochure">
    <section class="panel panel-left">
      <div class="director-photo" role="img" aria-label="Photo of the smiling medical director in a white coat"></div>
      <div class="portrait-frame">
        <div class="portrait-photo" role="img" aria-label="Portrait photo of the medical director"></div>
      </div>
      <p class="left-copy first">Lorem ipsum dolor sit amet, consectetuer adipiscing elit, sed diam nonummy nibh euismod Lorem ipsum dolor sit amet, Lorem ipsum dolor sit amet, consectetuer adipiscing elit, sed diam nonummy nibh euismod Lorem ipsum dolor sit amet, consectetuer adipiscing elit, sed diam nonummy nibh euismod</p>
      <p class="left-copy second">Lorem ipsum dolor sit amet, consectetuer adipiscing elit, sed diam nonummy nibh euismod Lorem ipsum dolor sit amet, Lorem ipsum dolor sit amet, consectetuer adipiscing elit, sed diam nonummy nibh euismod Lorem ipsum dolor sit amet, consectetuer adipiscing elit, sed diam nonummy nibh euismod</p>
    </section>

    <section class="panel panel-center">
      <svg class="science-art" viewBox="0 0 371 830">
        <defs>
          <linearGradient id="dnaGlow" x1="0" y1="0" x2="1" y2="1">
            <stop offset="0" stop-color="#4b3fc4"/>
            <stop offset="1" stop-color="#22309a"/>
          </linearGradient>
        </defs>
        <path role="img" aria-label="Illustration of a glowing DNA double helix"
              d="M0,445 Q30,690 371,830 L0,830 Z" fill="url(#dnaGlow)"/>
        <path d="M0,445 Q30,690 371,830" fill="none" stroke="#ffffff" stroke-width="4"/>
      </svg>
      <h2 class="services-title">Our Services</h2>
      <div class="services-box">
        <p>Lorem ipsum dolor sit amet, consectetuer adipiscing elit, sed diam nonummy nibh euismod Lorem ipsum dolor sit amet, Lorem ipsum dolor sit amet, consectetuer adipiscing elit, sed diam nonummy nibh euismod Lorem ipsum dolor sit amet, consectetuer adipiscing elit, sed diam nonummy nibh euismod</p>
        <p>Lorem ipsum dolor sit amet, consectetuer adipiscing elit, sed diam nonummy nibh euismod Lorem ipsum dolor sit amet, Lorem ipsum dolor sit amet, consectetuer adipiscing elit, sed diam nonummy nibh euismod Lorem ipsum dolor sit amet, consectetuer adipiscing elit, sed diam nonummy nibh euismod</p>
      </div>
    </section>

    <section class="panel panel-right">
      <div class="scanner-photo" role="img" aria-label="Photo of an MRI scanner with patient table in a bright clinical room"></div>
      <h3 class="right-headline">Lorem ipsum dolor sit<br>amet, consectetuer<br>adipiscing elit, sed<br>diam nonummy nibh<br>euismod</h3>
      <p class="right-body">Everything is totally<br>confidential.<br>VitaLens is a division of<br>Coral Ridge Diagnostic<br>Centers</p>
    </section>
  </main>
</body>
</html>
```